Thank You For Shopping / Hair Care Tips

I need “Thank You For Shopping”
Post cards made for my hair business !
I added pictures of post cards that I really like . I also added my LunaVex Wigs logo for you guys to use

I want the backside of the flyer to have hair care tips !
I want people to have full directions on how to care for their wigs

Target Market(s)

Im marking to young woman to older middle aged woman
Ages 23-66 . I want my flyer to look mature And classy

Industry/Entity Type

Hair And Beauty

Font styles to use
Serif
Script

Colors
e34699
e34298
e34398

Requirements
Must have
• The flyer must have the Instagram logo with my Instagram name next to it @luna.vex.wigs__
• Also it must have my “Luna Vex Wigs” logo that I’ve uploaded in the pictures section .
• Flyer had to be two sides . One side “ thank you for shopping “ side two “hair care tips”
• My website must be on the flyer - www.lunavexwigs.example
• The flyer must match the colors of my logo
• All white . With the pink and glitter sliver you see on my logo
Nice to have
• Nice to have a glitter border
Should not have
• The flyer should not have different colors that don’t match my logo
• It shouldn’t be made without having my Instagram or website on the flyer

```html
<!DOCTYPE html>
<html lang="en">
<head>
<meta charset="utf-8">
<title>Luna Vex Wigs – Thank You Postcard</title>
<link rel="stylesheet" href="https://fonts.googleapis.com/css2?family=Kaushan+Script&family=Alegreya:wght@400;500&family=Open+Sans:wght@700&display=swap">
<style>
  :root {
    --pink: #e34398;
    --pink-shadow: #e9c9da;
    --white: #ffffff;
    --paper: #f8f8f9;
    --silver-light: #d9d9dc;
    --silver-mid: #b3b3b8;
    --silver-dark: #8e8e94;
    --ink: #3a3a3a;
    --backdrop: #e7e7e9;
  }
  * { box-sizing: border-box; margin: 0; padding: 0; }
  html, body { width: 1200px; height: 800px; overflow: hidden; }
  body {
    background: var(--backdrop);
    position: relative;
    font-family: "Alegreya", Georgia, serif;
    color: var(--ink);
  }
  .postcard {
    position: absolute;
    top: 200px;
    width: 560px;
    height: 400px;
    box-shadow: 0 6px 18px rgba(0,0,0,.12);
  }
  .postcard--front { left: 30px; }
  .postcard--back { left: 610px; }

  .glitter-frame {
    position: absolute;
    inset: 0;
    background:
      radial-gradient(circle at 20% 30%, var(--silver-light), transparent 60%),
      radial-gradient(circle at 80% 70%, var(--silver-light), transparent 60%),
      linear-gradient(135deg, var(--silver-mid), var(--silver-dark) 50%, var(--silver-mid));
  }
  .card-face {
    position: absolute;
    inset: 24px;
    background: var(--paper);
  }
  .pink-band {
    position: absolute;
    left: 0;
    right: 0;
    background: var(--pink);
    box-shadow: 0 6px 0 var(--pink-shadow);
  }

  /* Front */
  .front-band { top: 50px; height: 76px; display: flex; align-items: center; justify-content: center; }
  .front-title {
    font-family: "Kaushan Script", cursive;
    font-weight: 400;
    font-size: 44px;
    color: var(--white);
    line-height: 1;
  }
  .brand-name {
    position: absolute;
    top: 192px;
    left: 0;
    right: 0;
    text-align: center;
    font-family: "Alegreya", Georgia, serif;
    font-weight: 500;
    font-size: 56px;
    color: var(--pink);
    letter-spacing: 1px;
  }
  .contact-row {
    position: absolute;
    left: 64px;
    bottom: 46px;
    display: flex;
    align-items: center;
    gap: 28px;
    font-size: 15px;
    color: var(--ink);
  }
  .contact-item { display: flex; align-items: center; gap: 8px; }
  .contact-icon { width: 16px; height: 16px; flex: none; }
  .social-dot {
    width: 14px; height: 14px; border-radius: 50%;
    border: 2px solid var(--pink);
  }

  /* Back */
  .tips-title {
    position: absolute;
    top: 26px;
    left: 0;
    right: 0;
    text-align: center;
    font-family: "Kaushan Script", cursive;
    font-weight: 400;
    font-size: 40px;
    line-height: 56px;
    color: var(--pink);
  }
  .tips-list {
    position: absolute;
    top: 94px;
    left: 36px;
    right: 18px;
    list-style: none;
    font-size: 10.5px;
    line-height: 14px;
  }
  .tips-list li, .bedtime-list li {
    position: relative;
    padding-left: 14px;
  }
  .tips-list li::before, .bedtime-list li::before {
    content: "";
    position: absolute;
    left: 0; top: 3px;
    width: 8px; height: 8px;
    border-radius: 50%;
    background: var(--pink);
  }
  .bedtime-band { top: 264px; height: 98px; padding: 10px 24px 0 50px; color: var(--white); }
  .bedtime-heading {
    font-family: "Open Sans", Arial, sans-serif;
    font-weight: 700;
    font-size: 12px;
    line-height: 16px;
    letter-spacing: .2px;
    margin-bottom: 2px;
  }
  .bedtime-list { list-style: none; font-size: 10.5px; line-height: 14px; }
  .bedtime-list li::before { background: var(--white); }
</style>
</head>
<body>

<section class="postcard postcard--front" aria-label="Thank you side">
  <div class="glitter-frame" role="img" aria-label="Silver glitter border"></div>
  <div class="card-face">
    <div class="brand-name">Luna Vex Wigs</div>
    <div class="contact-row">
      <span class="contact-item">
        <svg class="contact-icon" viewBox="0 0 16 16" fill="none" stroke="var(--pink)" stroke-width="1.4" aria-hidden="true">
          <circle cx="8" cy="8" r="7"/>
          <ellipse cx="8" cy="8" rx="3" ry="7"/>
          <line x1="1" y1="8" x2="15" y2="8"/>
        </svg>
        www.lunavexwigs.example
      </span>
      <span class="contact-item">
        <span class="social-dot" aria-hidden="true"></span>
        @luna.vex.wigs__
      </span>
    </div>
  </div>
  <div class="pink-band front-band">
    <h1 class="front-title">Thank You For Shopping</h1>
  </div>
</section>

<section class="postcard postcard--back" aria-label="Hair care tips side">
  <div class="glitter-frame" role="img" aria-label="Silver glitter border"></div>
  <div class="card-face">
    <h2 class="tips-title">Hair Care Tips</h2>
    <ul class="tips-list">
      <li>Apply moisture rich Conditioner and comb hair, starting with the ends working your way up to your scalp</li>
      <li>Leave Conditioner in for at least 15 minutes or more</li>
      <li>Do not message the hair</li>
      <li>Rinse thoroughly</li>
      <li>Scrunch hair gently to enhance the curls (for wavy/curly patterns)</li>
      <li>When damp, apply a dime size of an anti-frizz alcohol free hair serum</li>
      <li>Let hair-dry</li>
      <li>Do not use oil products or excensive products on curly hair, it will cause hair to tangle</li>
    </ul>
  </div>
  <div class="pink-band bedtime-band">
    <h3 class="bedtime-heading">BED TIME CARE</h3>
    <ul class="bedtime-list">
      <li>Before going to bed, braid your hair into one loose large braid and wear a satin scraf or bonnet</li>
      <li>After waking up, undo braid and comb using a wide tooth comb (or paddle brush) through beginning at the ends and working your way up to roots</li>
      <li>Style as needed</li>
    </ul>
  </div>
</section>

</body>
</html>
```